Need a sleek, professional business card design for a Web Development business

I need a unique business card designed for a web development company. It is also the parent company for any ventures I do, such as my ClipWave channel, startup ideas I have, etc. I am the single member of "Bright Harbor Code LLC." I will attach my basic logo here, so you will see the current color scheme and have the asset available. Thank you!

Target Market(s)

Startups, SMB's, Professionals

Industry/Entity Type

Business

Font styles to use
Other font styles liked:
• Lovello for headings is what I use, but not necessary.

Colors

Designer to choose colors to be used in the design.

Requirements
Nice to have
• Sleek is the word. Professional, modern, dark.
Should not have
• Any work from someone else's design. Lacking originality.

```html
<!DOCTYPE html>
<html lang="en">
<head>
<meta charset="utf-8">
<title>Bright Harbor Code LLC – Business Card</title>
<link rel="stylesheet" href="https://fonts.googleapis.com/css2?family=Source+Sans+3:ital,wght@0,600;0,700;1,600&display=swap">
<style>
  :root {
    --backdrop: #dedede;
    --card-white: #ffffff;
    --swoosh-grey: #e3e3e3;
    --ink-dark: #262626;
    --orange-warm: #f2584f;
    --orange-bright: #ff8a45;
    --band-deep: #ee3b22;
    --band-light: #ffa25a;
    --text-light: #ffffff;
  }
  html, body {
    margin: 0;
    padding: 0;
    width: 1200px;
    height: 897px;
    overflow: hidden;
    background: var(--backdrop);
  }
  .business-card {
    position: absolute;
    left: 166px;
    top: 141px;
    width: 869px;
    height: 496px;
  }
  .business-card svg { display: block; }
  .company-name {
    font-family: "Source Sans 3", sans-serif;
    font-weight: 700;
    font-size: 33px;
    fill: var(--text-light);
  }
  .contact-text {
    font-family: "Source Sans 3", sans-serif;
    font-style: italic;
    font-weight: 600;
    font-size: 24px;
    fill: var(--text-light);
  }
  .brand-name {
    font-family: "Source Sans 3", sans-serif;
    font-weight: 700;
    font-size: 20px;
    fill: var(--ink-dark);
  }
  .contact-icon { fill: var(--text-light); }
  .contact-icon-line { fill: none; stroke: var(--text-light); stroke-width: 2; }
</style>
</head>
<body>
<div class="business-card">
  <svg width="869" height="496" viewBox="0 0 869 496" xmlns="http://www.w3.org/2000/svg">
    <defs>
      <linearGradient id="orangeField" x1="0" y1="0" x2="1" y2="1">
        <stop offset="0" stop-color="var(--orange-warm)"/>
        <stop offset="1" stop-color="var(--orange-bright)"/>
      </linearGradient>
      <clipPath id="orangeArea">
        <path d="M268 0 H869 V496 H280 C380 420 458 330 458 248 C458 170 380 80 268 0 Z"/>
      </clipPath>
    </defs>

    <!-- card base -->
    <rect class="card-base" width="869" height="496" fill="var(--card-white)"/>

    <!-- grey swoosh -->
    <path class="swoosh" d="M118 0 H268 C380 80 458 170 458 248 C458 330 380 420 280 496 H126 C240 420 320 330 320 248 C320 170 240 80 118 0 Z" fill="var(--swoosh-grey)"/>

    <!-- orange panel with bands -->
    <g class="info-panel" clip-path="url(#orangeArea)">
      <rect width="869" height="496" fill="url(#orangeField)"/>
      <rect class="band" x="0" y="122" width="869" height="63" fill="var(--band-deep)" opacity="0.55"/>
      <rect class="band" x="0" y="188" width="869" height="63" fill="var(--band-deep)" opacity="0.45"/>
      <rect class="band" x="0" y="251" width="869" height="35" fill="var(--band-light)" opacity="0.6"/>
      <rect class="band" x="0" y="286" width="869" height="46" fill="var(--band-deep)" opacity="0.4"/>
      <rect class="band" x="0" y="337" width="869" height="44" fill="var(--band-deep)" opacity="0.4"/>
      <rect class="band" x="0" y="386" width="869" height="45" fill="var(--band-deep)" opacity="0.4"/>
    </g>

    <!-- white divider curve -->
    <path class="divider" d="M268 0 C380 80 458 170 458 248 C458 330 380 420 280 496" fill="none" stroke="var(--card-white)" stroke-width="6"/>

    <!-- brand block -->
    <rect class="brand-mark" x="118" y="176" width="80" height="80" fill="var(--ink-dark)"/>
    <text class="brand-name" x="158" y="292" text-anchor="middle">Bright Harbor Code</text>

    <!-- company heading -->
    <text class="company-name" x="487" y="96">Bright Harbor Code LLC</text>

    <!-- name and title -->
    <text class="contact-text" x="484" y="161">Your Name</text>
    <text class="contact-text" x="484" y="226">job title</text>

    <!-- address -->
    <path class="contact-icon" d="M482 292 a12 12 0 0 1 12 12 c0 9 -12 21 -12 21 c0 0 -12 -12 -12 -21 a12 12 0 0 1 12 -12 Z M482 299 a5 5 0 1 0 0.01 0 Z" fill-rule="evenodd"/>
    <text class="contact-text" x="523" y="315">Address Line</text>

    <!-- phone -->
    <path class="contact-icon" d="M472 343 l6 -3 l5 9 l-4 3 c2 6 6 10 11 13 l3 -4 l8 6 l-3 6 c-14 0 -26 -16 -26 -30 Z"/>
    <text class="contact-text" x="523" y="366">Phone</text>

    <!-- website -->
    <g class="contact-icon-line">
      <circle cx="483" cy="408" r="15"/>
      <ellipse cx="483" cy="408" rx="7" ry="15"/>
      <line x1="468" y1="408" x2="498" y2="408"/>
      <line x1="471" y1="400" x2="495" y2="400"/>
      <line x1="471" y1="416" x2="495" y2="416"/>
      <line x1="483" y1="393" x2="483" y2="423"/>
    </g>
    <text class="contact-text" x="523" y="416">Website</text>
  </svg>
</div>
</body>
</html>
```